KELBRO INSULATION WEB PAGE
WEB PAGE
THANK YOU VELNOX MEDIA,AND THANK YOU TO ALL WHO PARTICIPATE.....GRACIAS
appreciate morel
I like the concept of a picture of a dream home,but i also like the stock picture on draft #31,because it tells you that can be a new but also show you the attic and it looks like a remodeling
Morel,
Thank you for giving me 4stars this is a original size which you will see on wide screen.
Many Thanks.
Hey Morel,
I have done few changes in my design please have a look and give me feedback & if you need any changes please let me know.
morel,
I will do changes as you mention and submit my draft again.
I do like what he wrote on draft # 16 and I like the colors and all the contents in draft # 18
Hi PH,
I am inn, design will submit soon.....Thanks
what happend with the drafts for fossils? i hope that you sen more the first ones were good
Can you upload your logo?
I THINK I DID HAVE A MISTAKE,I WANT THE URL TO BE " kelbroinsulation.com "i was thinking that you were asking for websites that i like.

```html
<!DOCTYPE html>
<html lang="en">
<head>
<meta charset="utf-8">
<title>Kelbro Insulation</title>
<link href="https://fonts.googleapis.com/css2?family=Arimo:wght@400;700&display=swap" rel="stylesheet">
<style>
  :root {
    --green: #62c700;
    --green-dark: #4ea300;
    --green-deep: #3f8a00;
    --page-grey: #e3e3e3;
    --panel: #f7f7f7;
    --ink: #222222;
    --ink-soft: #555555;
    --footer: #343434;
    --footer-mark: #6a6a6a;
    --white: #ffffff;
  }
  * { box-sizing: border-box; margin: 0; padding: 0; }
  html, body { width: 1200px; height: 939px; overflow: hidden; }
  body {
    position: relative;
    font-family: "Arimo", Arial, sans-serif;
    background: var(--page-grey);
    color: var(--ink);
  }
  .top-band {
    position: absolute; left: 0; top: 0; width: 1200px; height: 255px;
    background: var(--green);
    overflow: hidden;
  }
  .top-band .panel-shade {
    position: absolute; background: var(--green-dark); opacity: .55;
  }
  .shade-a { left: 325px; top: 0; width: 200px; height: 150px; }
  .shade-b { left: 380px; top: 60px; width: 160px; height: 195px; opacity: .35 !important; }
  .nav-active {
    position: absolute; left: 652px; top: 0; width: 96px; height: 157px;
    background: var(--green-deep);
  }
  .brand {
    position: absolute; left: 152px; top: 0; width: 173px; height: 145px;
    background: var(--panel);
    display: flex; align-items: center; justify-content: center; gap: 8px;
  }
  .brand-square { width: 16px; height: 16px; background: var(--green-deep); flex: none; }
  .brand-name { font-size: 15px; font-weight: 700; color: var(--green-deep); line-height: 1.1; }
  .main-nav {
    position: absolute; top: 121px; left: 0; width: 1200px;
  }
  .main-nav a {
    position: absolute; color: var(--white); font-size: 15px; text-decoration: none; white-space: nowrap;
  }
  .content {
    position: absolute; left: 152px; top: 160px; width: 908px; height: 670px;
    background: var(--panel);
  }
  .hero {
    position: absolute; left: 152px; top: 160px; width: 908px; height: 347px;
    background: linear-gradient(180deg, #8fa6c9 0%, #c9d3df 45%, #7c6a5c 70%, #5a4a3c 100%);
  }
  .hero-caption {
    position: absolute; left: 0; bottom: 0; width: 100%; height: 139px;
    background: rgba(0,0,0,.72); padding: 26px 26px 0 26px; color: var(--white);
  }
  .hero-caption h1 { font-size: 34px; font-weight: 400; margin-bottom: 12px; }
  .hero-caption p { font-size: 12px; font-weight: 700; line-height: 1.4; width: 600px; }
  .gallery-intro { position: absolute; left: 178px; top: 528px; width: 300px; }
  .gallery-intro h2 { font-size: 15px; font-weight: 700; margin-bottom: 8px; }
  .gallery-intro p { font-size: 11px; line-height: 1.35; color: var(--ink-soft); }
  .thumb { position: absolute; top: 520px; height: 127px; }
  .thumb-1 { left: 492px; width: 124px; background: linear-gradient(135deg, #d9c24a, #7d6b3a); }
  .thumb-2 { left: 624px; width: 124px; background: linear-gradient(135deg, #b49a78, #e4dccd); }
  .thumb-3 { left: 756px; width: 157px; background: linear-gradient(135deg, #8a6a44, #d8d2c6); }
  .thumb-4 { left: 921px; width: 139px; background: linear-gradient(135deg, #a05a40, #5c4538); }
  .divider { position: absolute; left: 152px; top: 655px; width: 908px; height: 1px; background: #cfcfcf; }
  .about { position: absolute; left: 182px; top: 672px; width: 660px; }
  .about h2 { font-size: 22px; font-weight: 700; margin-bottom: 6px; }
  .about .lead { font-size: 11.5px; font-weight: 700; line-height: 1.4; margin-bottom: 10px; }
  .about p { font-size: 11px; line-height: 1.4; color: var(--ink-soft); }
  .site-footer {
    position: absolute; left: 0; top: 830px; width: 1200px; height: 109px;
    background: var(--footer);
  }
  .footer-brand {
    position: absolute; left: 142px; top: 36px; display: flex; align-items: center; gap: 10px;
  }
  .footer-brand .brand-square { background: var(--footer-mark); width: 20px; height: 20px; }
  .footer-brand span { font-size: 22px; font-weight: 700; color: var(--footer-mark); }
</style>
</head>
<body>
  <header class="top-band">
    <div class="panel-shade shade-a"></div>
    <div class="panel-shade shade-b"></div>
  </header>
  <div class="nav-active"></div>
  <div class="brand">
    <span class="brand-square"></span>
    <span class="brand-name">KELBRO<br>INSULATION</span>
  </div>
  <nav class="main-nav">
    <a style="left:587px">Home</a>
    <a style="left:675px">Service</a>
    <a style="left:767px">Gallery</a>
    <a style="left:866px">About Us</a>
    <a style="left:965px">Contact Us</a>
  </nav>

  <main class="content"></main>

  <section class="hero" role="img" aria-label="Photo of a large two-storey house with dormer windows under a blue sky">
    <div class="hero-caption">
      <h1>Lorem Ipsum Dolor sit Arnet</h1>
      <p>Lorem ipsum dolor sit amet, consectetur adipiscing elit. Praesent ultrices luctus libero, sit amet fermentum elit ultrices vel. Curabitur ligula lacus, vehicula eget dictum quis, fringilla eget magna. Suspendisse accumsan</p>
    </div>
  </section>

  <section class="gallery-intro">
    <h2>Gallery</h2>
    <p>Lorem ipsum dolor sit amet, consectetur adipiscing elit. Praesent ultrices luctus libero, sit amet fermentum elit ultrices vel. Curabitur ligula lacus, vehicula eget dictum quis, fringilla eget magna. Suspendisse accumsan</p>
  </section>
  <div class="thumb thumb-1" role="img" aria-label="Yellow insulation batt being handled"></div>
  <div class="thumb thumb-2" role="img" aria-label="Worker spraying foam insulation"></div>
  <div class="thumb thumb-3" role="img" aria-label="Attic rafters with blown insulation"></div>
  <div class="thumb thumb-4" role="img" aria-label="Installer spraying insulation between wall studs"></div>

  <div class="divider"></div>

  <section class="about">
    <h2>Lorem Ipsum</h2>
    <p class="lead">Lorem ipsum dolor sit amet, consectetur adipiscing elit. Praesent ultrices luctus libero, sit amet fermentum elit ultrices vel. Curabitur ligula lacus, vehicula eget dictum quis, fringilla eget magna. Suspendisse accumsan</p>
    <p>Lorem ipsum dolor sit amet, consectetur adipiscing elit. Praesent ultrices luctus libero, sit amet fermentum elit ultrices vel. Curabitur ligula lacus, vehicula eget dictum quis, fringilla eget magna. Suspendisse accumsan lacus at mi faucibus consequat. Maecenas dolor velit, fringilla non fermentum ut, placerat in sapien. Sed mi augue, scelerisque in consectetur eu, interdum id risus. Vestibulum et tellus vitae massa egestas auctor. Sed malesuada ultricies magna a mattis. Suspendisse potenti. Nam tristique mollis enim non feugiat. Morbi mollis dictum eros id suscipit.</p>
  </section>

  <footer class="site-footer">
    <div class="footer-brand">
      <span class="brand-square"></span>
      <span>KELBRO INSULATION</span>
    </div>
  </footer>
</body>
</html>
```